Up to the Challenge? Canadian based consulting company needs a two sided business card design

A Canadian based security risk management consulting company needs a two-sided business card design. What we do is provide advice and guidance related to emergency, security and business continuity management for small, medium and large companies to help ensure the protection of their people, assets, information, services, operations and reputation.

The final design should be simple, only one or two colours, eye catching, professional and one that makes people look at three or more times just because it looks so darn good.

I have include examples of business cards I like.

Target Market(s)

Small, medium and large companies.

Industry/Entity Type

Security

Contact Information for Business Card

Business Card Size: Standard size of 3.5" (89mm) x 2.0" (51mm) - (see full specifications and guides on PRINTA's website if required)
Card Stock: Looking to use PRINTA's Velda 32pt stock textured paper - seam colour either chili red or black
Business Name: The Harrowfield Group
Website: www.theharrowfieldgroup.example
Telephone: (555)214-0397
Name: Dana Forsythe
Position: Principle
e-mail: Dana.Forsythe@theharrowfieldgroup.example

Font styles to use
Serif

Colors
ec1f27
000000
9d9d9d
aaaaaa
606060

Requirements
Must have
• - "The Harrowfield Group" logo (see uploaded files). I have included grey scale and colour versions.
• - Business card details (as above)
Nice to have
• - One side black or grey scale.
• - Other side would likely be white.
• - Everyone likes the silver logo on the black background.
• - Small element of colour i.e. red but I'm leaning more to greyscale.
Should not have
• - A lot of colour. Keep it simple.

```html
<!DOCTYPE html>
<html lang="en">
<head>
<meta charset="utf-8">
<title>The Harrowfield Group – Business Card</title>
<link rel="stylesheet" href="https://fonts.googleapis.com/css2?family=Cinzel:wght@500&family=Open+Sans:wght@400;600&display=swap">
<style>
  :root {
    --backdrop: #e8e5e2;
    --card-black: #000000;
    --card-white: #ffffff;
    --silver: #d9d9d9;
    --grey-light: #aaaaaa;
    --grey-mid: #9d9d9d;
    --grey-dark: #606060;
    --text-white: #ffffff;
  }
  * { margin: 0; padding: 0; box-sizing: border-box; }
  html, body { width: 1200px; height: 900px; overflow: hidden; }
  body { background: var(--backdrop); position: relative; font-family: "Open Sans", Arial, sans-serif; }

  .card { position: absolute; box-shadow: 0 6px 18px rgba(0,0,0,.18); overflow: hidden; }

  /* Front: black side with contact details */
  .card-front {
    left: 238px; top: 62px; width: 555px; height: 343px;
    background:
      linear-gradient(180deg,
        var(--card-black) 0%,
        var(--card-black) 46%,
        #2a2a2a 52%,
        #8a8a8a 60%,
        #4a4a4a 72%,
        #1a1a1a 84%,
        var(--card-black) 100%);
    color: var(--text-white);
  }
  .person { position: absolute; left: 28px; top: 26px; }
  .person-name { font-size: 18px; font-weight: 600; line-height: 1.2; }
  .person-title { font-size: 14px; line-height: 1.3; }

  .company-name {
    font-family: "Cinzel", Georgia, serif; font-weight: 500;
    color: var(--text-white); text-align: center; line-height: 1;
  }
  .card-front .company-name { position: absolute; right: 32px; top: 94px; }
  .company-name .line-main { display: block; font-size: 26px; letter-spacing: .5px; }
  .company-name .line-sub { display: block; font-size: 19px; letter-spacing: 3px; margin-top: 4px; }

  .contacts { position: absolute; left: 28px; top: 224px; list-style: none; }
  .contacts li { display: flex; align-items: center; font-size: 14px; line-height: 20px; }
  .contacts svg { width: 11px; height: 11px; margin-right: 9px; fill: var(--text-white); flex: none; }

  /* Back: white side with the company name */
  .card-back {
    left: 457px; top: 518px; width: 560px; height: 344px;
    background: var(--card-white);
  }
  .card-back .company-name {
    position: absolute; left: 0; right: 0; top: 150px; color: var(--grey-dark);
  }
  .card-back .company-name .line-main { font-size: 30px; }
  .card-back .company-name .line-sub { font-size: 22px; }
</style>
</head>
<body>

  <section class="card card-front">
    <div class="person">
      <p class="person-name">Dana Forsythe</p>
      <p class="person-title">Principle</p>
    </div>

    <p class="company-name">
      <span class="line-main">THE HARROWFIELD</span>
      <span class="line-sub">GROUP</span>
    </p>

    <ul class="contacts">
      <li>
        <svg viewBox="0 0 12 12" aria-hidden="true"><path d="M2.4 0.6 4.2 2.8 3.2 4.1c.7 1.6 2 2.9 3.6 3.7l1.3-1 2.3 1.7-.9 2.1C5.2 10.5 1.4 6.8 0.5 1.6Z"/></svg>
        (555)214-0397
      </li>
      <li>
        <svg viewBox="0 0 12 12" aria-hidden="true"><path d="M0.5 2.5h11v7h-11Z M1.3 3.2 6 6.6l4.7-3.4" fill="none" stroke="#fff" stroke-width="1.1"/></svg>
        Forsythe@theharrowfieldgroup.example
      </li>
      <li>
        <svg viewBox="0 0 12 12" aria-hidden="true"><circle cx="6" cy="6" r="5.5"/><path d="M6 .5v11M.5 6h11M6 .5c-2.5 3-2.5 8 0 11M6 .5c2.5 3 2.5 8 0 11" fill="none" stroke="#000" stroke-width=".7"/></svg>
        www.theharrowfieldgroup.example
      </li>
    </ul>
  </section>

  <section class="card card-back">
    <p class="company-name">
      <span class="line-main">THE HARROWFIELD</span>
      <span class="line-sub">GROUP</span>
    </p>
  </section>

</body>
</html>
```